KVR Inc Web Design

WHAT ARE WE DOING?
We are developing a new website look and feel for a new company called KVR Inc. This new look and feel should include colors, design elements, choice of photography and other imagery, fonts, and other user experience elements.

WHAT DO THEY DO?
KVR, Inc, makes tools for researchers who are studying protein-protein interactions. These molecules are the basic tools of biology, and serve as key targets for drug developers and disease researchers. The world of proteins is enormously complex, and companies like KVR provide researchers with critical tools that help them elucidate this world.

WHO ARE WE TALKING TO?
The target audience for this website are professional scientists working in university research or biopharma drug development. They are highly sophisticated consumers looking for key tools that will advance their research.

WHAT DO WE WANT THEM TO DO?
The site is an information resource for the customer exploring the tools that KVR sells and the scientific issues surrounding protein-protein interactions. They should be able to navigate easily to their content of choice, while the whole site should convey a professionalism that enhanced KVR’s credibility.

WHAT DOES THE KVR BRAND STAND FOR?
KVR stands for illumination. Proteins are challenging to study, and KVR exists to help shed light on their workings.

WHAT ARE THE KEY VALUES OF THE KVR BRAND?
Integrity. Innovation. Insight.

WHAT ARE THE EXECUTIONAL MANDITORIES?
The look and feel is completely up for grabs. Nothing is off the table.

WHAT ARE THE DELIVERABLES?
We need new designs for the following templates:
http://cms.orvadeltaworks.com/
http://cms.orvadeltaworks.com/products-and-services/instruments-3/bench-top-instruments/
http://cms.orvadeltaworks.com/category/lab-study/

```html
<!DOCTYPE html>
<html lang="en">
<head>
<meta charset="utf-8">
<title>KVR Inc — Bench Top Instruments</title>
<link href="https://fonts.googleapis.com/css2?family=Source+Sans+3:wght@300;400;600&display=swap" rel="stylesheet">
<style>
:root{
  --orange:#f7a935;
  --orange-light:#fdc56a;
  --orange-dark:#e8901c;
  --nav-text:#4a3416;
  --ink:#3d3d3d;
  --body-text:#5c5c5c;
  --muted:#8a8a8a;
  --line:#dcdcdc;
  --panel:#f6f6f6;
  --sidebar-head:#ececec;
  --charcoal:#3f3f3f;
  --footer:#434343;
  --footer-text:#e6e6e6;
  --footer-muted:#b9b9b9;
  --white:#ffffff;
}
*{box-sizing:border-box;margin:0;padding:0}
html,body{width:1200px;height:1149px;overflow:hidden;background:var(--white)}
body{position:relative;font-family:"Source Sans 3",sans-serif;color:var(--body-text)}
.top-rule{position:absolute;left:0;top:0;width:1200px;height:5px;background:#e4e4e4}

.brand{position:absolute;left:89px;top:29px;width:227px;height:52px;background:#f5f5f5;display:flex;align-items:center;padding-left:22px;overflow:hidden}
.brand-name{font-size:40px;font-weight:300;letter-spacing:8px;color:#4a4a4a;line-height:1;white-space:nowrap}

.search{position:absolute;left:839px;top:52px;width:248px;height:31px;border:1px solid #d5d5d5;display:flex;background:var(--white)}
.search-field{flex:1;font-size:12px;font-style:italic;color:#9a9a9a;padding:8px 12px}
.search-button{width:32px;border-left:1px solid #d5d5d5;display:flex;align-items:center;justify-content:center;background:#f4f4f4}

.main-nav{position:absolute;left:110px;top:103px;width:980px;height:49px;display:flex;background:linear-gradient(#fdc86f,var(--orange) 55%,#f39d24);border-bottom:1px solid var(--orange-dark)}
.main-nav a{display:flex;align-items:center;justify-content:center;font-size:18px;color:var(--nav-text);text-decoration:none;border-right:1px solid #e79422;box-shadow:1px 0 0 #fdd08a;white-space:nowrap}
.main-nav a:last-child{border-right:0;box-shadow:none}

.hero{position:absolute;left:0;top:152px;width:1200px;height:204px;background:repeating-linear-gradient(135deg,#efefef 0 2px,#fafafa 2px 5px)}
.hero-photo{position:absolute;left:111px;top:0;width:979px;height:204px;background:linear-gradient(90deg,#8b9095 0%,#c9cdd1 25%,#e9ebed 50%,#d8dadc 70%,#eef0f1 100%)}
.hero-label{position:absolute;left:792px;top:114px;width:256px;height:52px;background:rgba(55,55,55,.92);border-bottom:5px solid var(--orange);color:var(--white);font-size:22px;font-weight:300;display:flex;align-items:center;padding-left:19px;letter-spacing:.3px;white-space:nowrap}

.sidebar{position:absolute;left:110px;top:399px;width:226px;height:212px;border:1px solid #e6e6e6;background:#fbfbfb}
.sidebar-title{height:44px;background:var(--sidebar-head);font-size:17px;color:var(--ink);display:flex;align-items:center;padding-left:22px}
.sidebar-group{padding:16px 0 0 25px;font-size:13.5px;color:var(--ink)}
.sidebar-list{list-style:none;margin-top:6px}
.sidebar-list li{font-size:13.5px;color:var(--body-text);line-height:24px;display:flex;align-items:center;gap:6px}
.sidebar-list li::before{content:"";border-left:5px solid #333;border-top:5px solid transparent;border-bottom:5px solid transparent}

.page-title{position:absolute;left:359px;top:392px;font-size:27px;font-weight:300;color:var(--ink);white-space:nowrap}
.product-photo{position:absolute;left:361px;top:435px;width:259px;height:164px;background:linear-gradient(160deg,#6f93b8,#dde7f0 55%,#f1c28a)}
.intro{position:absolute;left:637px;top:432px;width:447px;font-size:13px;font-weight:300;line-height:19px;color:var(--body-text)}
.intro p{margin-bottom:10px}

.tabs{position:absolute;left:364px;top:634px;height:36px}
.tab{position:absolute;top:0;height:36px;display:flex;align-items:center;justify-content:center;font-size:17px;font-weight:400;color:var(--white);background:linear-gradient(#fbb548,#f29a22);border:1px solid #e8911f;border-bottom:0;text-shadow:0 1px 1px rgba(150,80,0,.45);white-space:nowrap}
.tab.is-active{background:linear-gradient(#5a5a5a,var(--charcoal));border-color:#333;text-shadow:none}

.tab-panel{position:absolute;left:363px;top:670px;width:728px;height:299px;border:1px solid var(--line);border-radius:2px;background:var(--white)}
.tab-photo{position:absolute;left:23px;top:27px;width:193px;height:128px;background:linear-gradient(135deg,#c5ccd4,#eef1f4 50%,#aeb6bf)}
.tab-copy{position:absolute;left:239px;top:26px;width:470px}
.tab-copy h2{font-size:20px;font-weight:400;color:var(--ink);margin-bottom:2px}
.tab-copy p{font-size:13px;font-weight:300;line-height:19.2px;color:var(--body-text);margin-bottom:19px}

.footer-rule{position:absolute;left:0;top:1027px;width:1200px;height:7px;background:#e3e3e3}
.site-footer{position:absolute;left:0;top:1034px;width:1200px;height:115px;background:var(--footer)}
.footer-links{position:absolute;left:113px;top:25px;font-size:15px;color:var(--footer-text);display:flex;gap:6px;white-space:nowrap}
.footer-links span.sep{color:var(--footer-text)}
.copyright{position:absolute;left:113px;top:55px;font-size:12.5px;font-weight:300;color:var(--footer-muted)}
.social{position:absolute;left:968px;top:24px;display:flex;gap:4px}
.social span{width:29px;height:29px;border-radius:50%;background:#f0f0f0;border:2px solid #d0d0d0}
</style>
</head>
<body>
<div class="top-rule"></div>

<header>
  <div class="brand"><span class="brand-name">KVR INC</span></div>
  <div class="search">
    <div class="search-field">Search here..</div>
    <div class="search-button">
      <svg width="16" height="16" viewBox="0 0 16 16" aria-hidden="true"><circle cx="6.5" cy="6.5" r="4.8" fill="none" stroke="#8a8a8a" stroke-width="2"/><line x1="10" y1="10" x2="14.5" y2="14.5" stroke="#8a8a8a" stroke-width="2.4" stroke-linecap="round"/></svg>
    </div>
  </div>
  <nav class="main-nav">
    <a style="width:165px">Company</a>
    <a style="width:201px">Product &amp; Services</a>
    <a style="width:185px">Learning Center</a>
    <a style="width:121px">Events</a>
    <a style="width:138px">KVR News</a>
    <a style="width:170px">Contact Us</a>
  </nav>
</header>

<section class="hero">
  <div class="hero-photo" role="img" aria-label="Photo of researchers in safety glasses working at a laboratory bench"></div>
  <div class="hero-label">PRODUCT OVERVIEW</div>
</section>

<aside class="sidebar">
  <div class="sidebar-title">PRODUCT OVERVIEW</div>
  <div class="sidebar-group">INSTRUMENTS
    <ul class="sidebar-list">
      <li>Bench Top Instruments</li>
      <li>Microscope Attachments</li>
    </ul>
  </div>
</aside>

<main>
  <h1 class="page-title">Bench Top Instruments</h1>
  <div class="product-photo" role="img" aria-label="Render of an automated bench top instrument with sample plates"></div>
  <div class="intro">
    <p>Maecenas imperdiet nisi eu justo dapibus, commodo venenatis massa tempus. Morbi consectetur sed justo vitae dictum. Ut semper tincidunt accumsan.</p>
    <p>Nunc suscipit dui in massa ultricies, ac sagittis velit pulvinar. In scelerisque id lectus eu facilisis. Morbi et nunc non nulla lobortis ultricies sit amet a turpis. Integer eget ullamcorper metus.</p>
    <p>Cras vitae nibh non dolor scelerisque porta.Nunc suscipit dui in massa ultricies, ac sagittis velit pulvinar. In scelerisque id lectus eu facilisis. Morbi et nunc non nulla lobortis ultricies siamet a turpis. Integer eget ullamcorper metus.</p>
  </div>

  <div class="tabs">
    <div class="tab is-active" style="left:0;width:114px">Overview</div>
    <div class="tab" style="left:119px;width:115px">Features</div>
    <div class="tab" style="left:240px;width:139px">Specifications</div>
    <div class="tab" style="left:384px;width:81px">FAQ’s</div>
    <div class="tab" style="left:470px;width:98px">Manuals</div>
  </div>

  <div class="tab-panel">
    <div class="tab-photo" role="img" aria-label="Photo of a compact white laboratory instrument"></div>
    <div class="tab-copy">
      <h2>Overview</h2>
      <p>Donec nec ipsum eget erat lacinia consectetur. Sed non turpis pretium, porttitor lorem eu, congue turpis. Vivamus viverra semper sem eget elementum. Aliquam augue libero, hendrerit a tortor vestibulum, rutrum suscipit ante. Curabitur a ligula ligula. In eget eros non metus elementum consequat id quis enim.</p>
      <p>Vivamus dignissim pharetra mi a tempor. Aenean pellentesque, arcu sed sodales vestibulum, nunc nulla molestie sem, ut imperdiet neque turpis sed purus. Nunc euis-mod tortor nec nibh venenatis convallis. Suspendisse magna augue, blandit et quam ac, fermentum dignissim purus. Curabitur tempor ac metus ut bibendum. Nulla id nisi semper, ornare nisi quis, laoreet dolor. Aliquam erat volutpat. Suspendisse ac metus sed orci mattis tempor ut eu lectus</p>
    </div>
  </div>
</main>

<div class="footer-rule"></div>
<footer class="site-footer">
  <div class="footer-links">
    <span>Home</span><span class="sep">|</span><span>Company</span><span class="sep">|</span><span>Products &amp; Services</span><span class="sep">|</span><span>Contact Us</span><span class="sep">|</span><span>Site Map</span>
  </div>
  <div class="copyright">© 2013 Company Name.&nbsp; All right reserved</div>
  <div class="social" aria-label="Social links"><span></span><span></span><span></span><span></span></div>
</footer>
</body>
</html>
```